eBook Cover_H. Vollmar-Tessen
Schnell und zuverlässoig,Änderungswünsche wurden umgehend ausgeführt. Vielen Dank für das tolle Cover zu meinem ersten Buch!
Zielgruppe
freie Roman-Autorin (Erstlingswerk)
Zielgruppe: Lesende (Erwachsene), Frauen
Charakterisierung: magisch-realistischer Familienroman, spielt im Europa der Jetzt-Zeit
Aufgabenstellung
Im ersten Schritt geht es um ein Cover für ein eBook, das aber bei Bedarf als Book on Demand gedruckt werden soll. Es wird daher später Anforderung bzgl. Dicke / Umfang des gedruckten Buches und einer Rückseite geben. Das gewählte Design soll dann dahingehend überarbeitet und finale Druckdaten zur Verfügung gestellt werden. Dies soll von vornherein berücksichtigt werden und im Preis enthalten sein.
Titel: Nebel über Glas, Funken im Moor
Autorinnenname: Henrike Vollmar-Tessen
des weiteren auf dem Cover: Roman

```html
<!DOCTYPE html>
<html lang="de">
<head>
<meta charset="utf-8">
<title>Nebel über Glas, Funken im Moor – Cover</title>
<link href="https://fonts.googleapis.com/css2?family=Open+Sans:wght@400&family=Gochi+Hand&display=swap" rel="stylesheet">
<style>
  :root {
    --page-bg: #ececec;
    --sky-deep: #2f4f9e;
    --sky-mid: #5f8fd6;
    --cloud: #e9eef7;
    --haze: #cfe0ec;
    --ridge: #6f6a8a;
    --ground: #8a7a5c;
    --ground-dark: #4a3f2c;
    --ink: #111111;
    --white: #ffffff;
  }
  * { margin: 0; padding: 0; box-sizing: border-box; }
  html, body {
    width: 1200px;
    height: 1200px;
    overflow: hidden;
    background: var(--page-bg);
  }
  .cover {
    position: absolute;
    left: 282px;
    top: 89px;
    width: 637px;
    height: 1022px;
    overflow: hidden;
  }
  .cover-photo {
    position: absolute;
    inset: 0;
    background:
      radial-gradient(ellipse 70% 45% at 30% 45%, rgba(233,238,247,0.9), rgba(233,238,247,0) 70%),
      linear-gradient(180deg,
        var(--sky-deep) 0%,
        var(--sky-mid) 30%,
        #8fb6e6 55%,
        var(--haze) 68%,
        var(--ridge) 68.5%,
        #8c89a6 71%,
        var(--cloud) 72%,
        #f3f6f8 84%,
        var(--ground) 88%,
        var(--ground-dark) 100%);
  }
  .author {
    position: absolute;
    top: 88px;
    left: 0;
    width: 100%;
    padding-left: 106px;
    font-family: "Open Sans", sans-serif;
    font-weight: 400;
    font-size: 37px;
    line-height: 1;
    color: var(--white);
    letter-spacing: 0.5px;
  }
  .title {
    position: absolute;
    left: 0;
    width: 100%;
    text-align: center;
    font-family: "Gochi Hand", cursive;
    font-weight: 400;
    color: var(--ink);
    line-height: 1;
  }
  .title-main { top: 244px; font-size: 80px; padding-left: 10px; }
  .title-sub { top: 356px; font-size: 58px; padding-left: 22px; }
  .genre {
    position: absolute;
    top: 958px;
    left: 0;
    width: 100%;
    text-align: center;
    font-family: "Open Sans", sans-serif;
    font-size: 31px;
    line-height: 1;
    color: var(--white);
  }
</style>
</head>
<body>
  <div class="cover">
    <div class="cover-photo" role="img" aria-label="Foto: Holzkreuz auf einem Berggipfel mit Bank, dahinter Nebelmeer, Bergkette und blauer Himmel mit Schleierwolken"></div>
    <p class="author">Henrike Vollmar-Tessen</p>
    <h1 class="title title-main">nebel über glas</h1>
    <p class="title title-sub">funken im moor</p>
    <p class="genre">Roman</p>
  </div>
</body>
</html>
```